New patented product needs a snazzy brochure

We are an equipment manufacturing company located in Sydney Australia. We require an A5 size 4 page brochure designed to promote a new product we are just about to launch.

Our new machine is called a sheet following system and is used in conjunction with brake presses (machines used to fold sheet and plate metal). It basically supports large sheets of metal in the folding process to save the arms and backs of operators.

You can see from the attached photos the actual machine is painted red and black. We would like some of that colour incorporated in the design of the brochure.

The machine is patented, as we are unique to other systems on the market. We can retrofit to any existing machine as well as be used with other brake presses in their factory. Our competitors' units can only be used on the break press machine they are installed on. If you have a second hand break press, we are your only option.

Two or more of the units are used in conjunction with a press brake, depending on it's length and the length of the material being folded.

I have now guaranteed this project.  More photos have been added as well as logo.  Text is being worked on now and will be uploaded very shortly.

Reason: Hi Guys I have extended the deadline as I have been out of the office until now and unable to give you feedback as well as upload a logo file. Thank you to all that have submitted and I hope this gives you a bit more breathing space due to my delayed responses. Cheers Megan

Target Market(s)

marketing the decision makers of sheet and plate metal work shops. They are 95% men, middle aged.

Industry/Entity Type

It Company

Requirements
Must have
• Must be A5 size utilizing all 4 pages. Photos that have been provided to be incorporated. If you don't want to use them all that is fine, I have provided probably more than needed.
Nice to have
• a small amount of metal graphic in there, but not over the top.
Should not have
• No old style fonts

```html
<!DOCTYPE html>
<html lang="en">
<head>
<meta charset="utf-8">
<title>Sheet Following System – Brochure Cover</title>
<link rel="stylesheet" href="https://fonts.googleapis.com/css2?family=PT+Sans:wght@400;700&display=swap">
<style>
  :root {
    --backdrop: #5b5b5b;
    --cover-dark: #232323;
    --cover-mid: #343434;
    --band-light: #d4d4d4;
    --band-shadow: #8c8c8c;
    --machine-red: #ec4a1f;
    --machine-red-deep: #c8380f;
    --concrete: #a7a29a;
    --concrete-light: #cdc9c1;
    --steel: #bfbfbf;
    --text-light: #f4f4f4;
    --text-muted: #d2d2d2;
    --silver: #e0e0e0;
  }
  * { box-sizing: border-box; margin: 0; padding: 0; }
  html, body {
    width: 1200px;
    height: 900px;
    overflow: hidden;
    background: var(--backdrop);
    font-family: "PT Sans", sans-serif;
  }
  .canvas {
    width: 1200px;
    height: 900px;
    display: flex;
    align-items: center;
    justify-content: center;
  }
  .cover {
    position: relative;
    width: 580px;
    height: 820px;
    background:
      radial-gradient(ellipse at 30% 55%, #3a3a3a 0%, transparent 60%),
      linear-gradient(170deg, var(--cover-mid) 0%, var(--cover-dark) 60%, #1c1c1c 100%);
    overflow: hidden;
    box-shadow: 0 18px 40px rgba(0,0,0,0.45);
  }

  /* Hero photo area */
  .cover-photo {
    position: absolute;
    left: 0; top: 0;
    width: 100%;
    height: 300px;
    background: linear-gradient(115deg,
      var(--machine-red) 0%,
      var(--machine-red-deep) 30%,
      #7d5a48 44%,
      var(--concrete) 56%,
      var(--concrete-light) 100%);
  }
  .cover-photo::after {
    content: "";
    position: absolute;
    inset: 0;
    background: linear-gradient(180deg, rgba(0,0,0,0.25) 0%, transparent 25%, transparent 80%, rgba(0,0,0,0.2) 100%);
  }

  .divider-band {
    position: absolute;
    left: 0; top: 300px;
    width: 100%;
    height: 14px;
    background: linear-gradient(180deg, var(--band-light) 0%, var(--steel) 45%, var(--band-shadow) 100%);
    box-shadow: 0 3px 6px rgba(0,0,0,0.5);
  }

  /* Brand stand-in */
  .brand {
    position: absolute;
    display: flex;
    align-items: flex-start;
    gap: 8px;
    color: var(--text-light);
  }
  .brand-mark {
    width: 11px; height: 11px;
    margin-top: 5px;
    background: var(--machine-red);
  }
  .brand-text { display: flex; flex-direction: column; gap: 3px; }
  .brand-name {
    font-size: 21px;
    font-weight: 700;
    letter-spacing: 1px;
    line-height: 1;
  }
  .brand-tagline {
    font-size: 9.5px;
    font-weight: 700;
    letter-spacing: 1px;
    text-transform: uppercase;
    line-height: 1.25;
    color: var(--text-light);
  }
  .brand--top {
    right: 24px; top: 18px;
    padding: 8px 10px;
    background: rgba(30,30,30,0.55);
  }
  .brand--cover { right: 60px; top: 412px; }
  .brand--cover .brand-tagline { color: var(--text-muted); }

  .cover-title {
    position: absolute;
    right: 24px;
    top: 340px;
    font-size: 42px;
    font-weight: 400;
    line-height: 1.1;
    color: var(--text-light);
    white-space: nowrap;
  }

  /* Product photo */
  .machine-photo {
    position: absolute;
    right: 0; top: 520px;
    width: 290px;
    height: 200px;
    background: linear-gradient(160deg,
      #d6d6d6 0%,
      #a9a9a9 28%,
      #4a4a4a 48%,
      #262626 62%,
      var(--machine-red-deep) 82%,
      var(--machine-red) 100%);
    border-top: 2px solid var(--silver);
    border-left: 2px solid var(--silver);
    box-shadow: -6px 6px 14px rgba(0,0,0,0.5);
  }

  .footer-rules {
    position: absolute;
    left: 0; bottom: 66px;
    width: 100%;
  }
  .footer-rules svg { display: block; }
  .footer-base {
    position: absolute;
    left: 0; bottom: 0;
    width: 100%;
    height: 56px;
    background: linear-gradient(180deg, #1e1e1e, #141414);
  }
</style>
</head>
<body>
<main class="canvas">
  <article class="cover">
    <div class="cover-photo" role="img" aria-label="Close-up photo of the red sheet following arm against a concrete factory wall"></div>

    <div class="brand brand--top">
      <span class="brand-mark"></span>
      <div class="brand-text">
        <span class="brand-name">KESTREL</span>
        <span class="brand-tagline">Kestrel Press Equipment Group</span>
      </div>
    </div>

    <div class="divider-band"></div>

    <h1 class="cover-title">Sheet Following System</h1>

    <div class="brand brand--cover">
      <span class="brand-mark"></span>
      <div class="brand-text">
        <span class="brand-name">KESTREL</span>
        <span class="brand-tagline">Kestrel Press Equipment Group</span>
      </div>
    </div>

    <div class="machine-photo" role="img" aria-label="Photo of the red and black sheet following unit mounted below a steel press brake"></div>

    <div class="footer-rules">
      <svg width="580" height="14" viewBox="0 0 580 14" aria-hidden="true">
        <rect x="0" y="0" width="580" height="3" fill="var(--silver)"/>
        <rect x="0" y="7" width="580" height="1.5" fill="var(--band-shadow)"/>
        <rect x="0" y="11" width="580" height="1" fill="#666"/>
      </svg>
    </div>
    <div class="footer-base"></div>
  </article>
</main>
</body>
</html>
```